Brochure Design Project

We need a brochure designed for our company, specifically targeted at our corporate business customers ... Banks, Financial Services, Government. The brochure needs to detail our services and what we have to offer.

It may be a brochure/booklet that we can give to clients when we meet them. It needs to have a very corporate look and feel and needs to align with our colour palette and logo.

Information is held on our website www.veltrexworldservices.com

Thank you everyone for being part of this project.  It was a very hard decision.

Target Market(s)

Corporate business and clients including banks, financial services, insurance and government.

Industry/Entity Type

Business

Requirements
Must have
• Must have a corporate and global feel to it.
Must have our logo and same or similar colour palette.

```html
<!DOCTYPE html>
<html lang="en">
<head>
<meta charset="utf-8">
<title>Veltrex World Services – Brochure Cover</title>
<link href="https://fonts.googleapis.com/css2?family=Arimo:wght@400;700&display=swap" rel="stylesheet">
<style>
  :root{
    --page:#e9e9ec;
    --ink-dark:#0a0a0d;
    --blue-deep:#0b2f7a;
    --blue-mid:#1565c0;
    --blue-bright:#2f8fe0;
    --silver:#c9ccd3;
    --cover-grey:#eeeef1;
    --navy:#1f2a6b;
    --text-dark:#222226;
    --link-blue:#1f6fc0;
    --white:#ffffff;
  }
  *{margin:0;padding:0;box-sizing:border-box}
  html,body{width:1200px;height:930px;overflow:hidden;background:var(--page)}
  body{font-family:"Arimo",Arial,sans-serif;position:relative}
  .brochure{position:absolute;left:98px;top:110px;width:1004px;height:710px;display:flex;box-shadow:0 4px 14px rgba(0,0,0,.25)}
  .panel{position:relative;width:502px;height:710px;overflow:hidden}
  .panel svg.bg{position:absolute;inset:0}

  /* back panel */
  .back{background:var(--ink-dark);border-right:1px solid #000}
  .company-title{position:absolute;left:60px;top:115px;color:var(--white);font-size:18px;font-weight:700}
  .solutions-heading{position:absolute;left:62px;top:184px;color:var(--white);font-size:21px;font-weight:700;word-spacing:3px}
  .solutions-list{position:absolute;left:62px;top:222px;list-style:none}
  .solutions-list li{color:var(--white);font-size:11.5px;font-weight:700;line-height:19px;display:flex;align-items:center}
  .solutions-list li::before{content:"";width:10px;height:10px;border-radius:50%;margin-right:9px;
    background:radial-gradient(circle at 35% 35%,#cfe6ff,var(--blue-mid) 60%,var(--blue-deep))}
  .contact{position:absolute;top:648px;color:var(--white);font-size:11px;line-height:14px}
  .contact.address{left:72px;text-align:right;width:156px}
  .contact.lines{left:268px}
  .contact b{font-weight:700}

  /* front panel */
  .front{background:var(--cover-grey)}
  .brand{position:absolute;left:0;right:0;top:420px;text-align:center;color:var(--navy);font-weight:700}
  .brand-mark{width:88px;height:88px;border-radius:50%;background:var(--blue-mid);margin:0 auto 16px}
  .brand-name{font-size:31px;letter-spacing:3px;line-height:32px}
  .brand-sub{font-size:17px;letter-spacing:2px;line-height:22px}
  .tagline{position:absolute;left:0;right:0;top:626px;text-align:center;color:var(--text-dark);font-size:12.5px;font-weight:700}
  .website{position:absolute;left:0;right:0;top:646px;text-align:center;color:var(--link-blue);font-size:10px;letter-spacing:2px}
</style>
</head>
<body>
<main class="brochure">

  <section class="panel back" aria-label="Back cover">
    <svg class="bg" width="502" height="710" viewBox="0 0 502 710">
      <defs>
        <linearGradient id="backBlue" x1="0" y1="0" x2="1" y2="0">
          <stop offset="0" stop-color="#0d3f9a"/><stop offset=".6" stop-color="#1d6fd0"/><stop offset="1" stop-color="#0b2f7a"/>
        </linearGradient>
        <linearGradient id="chessTones" x1="0" y1="0" x2="0" y2="1">
          <stop offset="0" stop-color="#141416"/><stop offset=".55" stop-color="#6b6a62"/><stop offset="1" stop-color="#2a2a2a"/>
        </linearGradient>
      </defs>
      <path d="M0 0H502V95C420 40 260 10 0 30Z" fill="url(#backBlue)"/>
      <path d="M0 30C200 12 360 30 502 98V110C360 50 200 40 0 62Z" fill="var(--silver)"/>
      <path d="M0 62C200 44 360 64 502 110V118C360 76 200 72 0 80Z" fill="#0d3f9a"/>
      <rect x="0" y="330" width="502" height="300" fill="url(#chessTones)" role="img" aria-label="Photo of chess pieces on a board with a fallen black king"/>
      <path d="M0 540C120 590 300 610 502 600V710H0Z" fill="url(#backBlue)"/>
      <path d="M0 532C130 588 300 604 502 594V604C300 614 120 598 0 552Z" fill="var(--silver)"/>
    </svg>
    <h1 class="company-title">Veltrex World Services Pty Ltd</h1>
    <h2 class="solutions-heading">For Solutions</h2>
    <ul class="solutions-list">
      <li>Banking &amp; Finance Solutions</li>
      <li>Business Solutions</li>
      <li>Community Solutions</li>
      <li>Environmental Solutions</li>
      <li>Global Solutions</li>
    </ul>
    <p class="contact address">PO Box 48, Harbour Street West<br>Victoria 8012, AUSTRALIA</p>
    <p class="contact lines"><b>T:</b> +61 (03) 9000 4821<br><b>E:</b> info@veltrexworldservices.com</p>
  </section>

  <section class="panel front" aria-label="Front cover">
    <svg class="bg" width="502" height="710" viewBox="0 0 502 710">
      <defs>
        <linearGradient id="frontPhoto" x1="0" y1="0" x2="0" y2="1">
          <stop offset="0" stop-color="#0a3f96"/><stop offset=".5" stop-color="#2b8fe0"/><stop offset="1" stop-color="#7fc4f2"/>
        </linearGradient>
      </defs>
      <path d="M0 0H502V130C430 230 240 300 0 280Z" fill="url(#frontPhoto)" role="img" aria-label="World map backdrop with silhouettes of business people"/>
      <path d="M0 280C240 300 430 230 502 130V150C430 250 240 312 0 292Z" fill="#0b2f7a"/>
      <path d="M0 292C240 312 430 250 502 150V158C430 262 240 318 0 300Z" fill="var(--white)"/>
      <path d="M0 300C240 318 430 262 502 158V170C430 274 240 326 0 308Z" fill="var(--blue-mid)"/>
    </svg>
    <div class="brand">
      <div class="brand-mark"></div>
      <div class="brand-name">VELTREX</div>
      <div class="brand-sub">WORLD SERVICES</div>
    </div>
    <p class="tagline">Specialists in transformational change &amp; sustainable solutions</p>
    <p class="website">www.veltrexworldservices.com</p>
  </section>

</main>
</body>
</html>
```